Web design for Digital Marketing Agency

Hello,
the name of our agency is "Bright Lantern" with the idea that we make BRIGHT LANTERN for our client count. You can find our logo attached. Use blue tone similar to it a modern sans serif form that fits the design.
We need a web design similar to this one:
https: // larkfield-studio. de /
What I like about this design:
- clear navigation with personalized Pic for phone number and clear call to action in nav bar (which is then repeated in hero image)
- the hero image having custom cartoon represtation giving a visual impression of what the company does (in our case paid adwords on different channels, like Wexly Ads, Tribbon etc; and analyzing data and optimizing the website based on that)
-a clear cut structure that goes on with similar cartoons when appropriate
- using bright background colors for sections
- lots of space so content can breath
The following sections are needed in this order:
-navbar
-hero image with text:
"Digital marketing for companies who know that BRIGHT LANTERN counts.
We always help you to achieve the best in every digital transaction. Because like in real life, you don't get a second channel for your first impression. "
Services Section:
1.) Paid advertising
2.) Analytics & Optimization
3.) Chatbots
4.) E-commerce shops
-Explaining the Service Secion (the section explaining the service that is chose by the user above 1/3 image / 2/3 text - image should also be a cartoon fitting in style to overall pic and representing the service that will be explained)
- Bright Lantern Concept
2 rings similar to above website
- the process section
- what customer are saying section
-contact form section
-footer
Target Market(s)
Companies seeking to increase sales online / generate new lead online. Main focus ecommerce but also traditional companies like real estate or lawyers
Number of Pages Required
1 page
Font styles to use
Look and feel
Each slider illustrates characteristics of the customer's brand and the style your logo design should communicate.

```html
<!DOCTYPE html>
<html lang="en">
<head>
<meta charset="utf-8">
<title>Bright Lantern – Digital Marketing Agency</title>
<link href="https://fonts.googleapis.com/css2?family=Poppins:wght@300;400;500;600;700&display=swap" rel="stylesheet">
<style>
:root{
  --blue:#2f9fd8;
  --blue-dark:#1f7fc0;
  --yellow:#f6b81c;
  --ink:#2b2b33;
  --body:#6d6d78;
  --pink:#fde8f2;
  --grey:#f3f3f4;
  --violet-a:#3f3fe0;
  --violet-b:#7420c4;
  --footer:#1c1c20;
  --line:#e4e4e8;
}
*{box-sizing:border-box;margin:0;padding:0}
html,body{width:1200px;height:3062px;overflow:hidden}
body{position:relative;font-family:'Poppins',sans-serif;color:var(--body);background:#fff;font-size:10px;line-height:1.55}
.abs{position:absolute}
.u{position:relative;display:inline-block}
.u::after{content:"";position:absolute;left:0;bottom:2px;width:48%;height:3px;background:var(--yellow);z-index:-1}
.btn{position:absolute;display:flex;align-items:center;justify-content:center;color:#fff;font-weight:600;font-size:10.5px;letter-spacing:.4px;background:linear-gradient(90deg,var(--violet-a),var(--violet-b));border-radius:2px}
.art{position:absolute;border-radius:6px}
.para{position:absolute;font-size:9.2px;line-height:1.5;color:var(--body)}
.para p{margin-bottom:11px}

/* header */
.topline{top:5px;left:704px;font-size:9.5px;color:var(--ink);display:flex;gap:14px;align-items:center}
.topline span{display:flex;align-items:center;gap:5px}
.brand{display:flex;align-items:center;gap:8px;font-weight:600;font-size:14px;color:var(--blue);letter-spacing:.2px}
.brand i{width:40px;height:40px;border-radius:50%;background:var(--blue);display:block}
.navbar{top:25px;left:532px;width:668px;height:43px;background:var(--blue);border-radius:22px 0 0 22px;display:flex;align-items:center;padding-left:30px;color:#fff;font-size:9.4px;font-weight:500;letter-spacing:.6px}
.navbar a{color:#fff;text-decoration:none}
.navbar .sep{margin:0 11px;opacity:.8}
.navbar .on{border-bottom:2px solid var(--yellow);padding-bottom:1px}

/* hero */
.eyebrow{top:197px;left:235px;font-size:12px;font-weight:600;color:var(--ink);letter-spacing:1px}
.hero-title{top:230px;left:235px;width:400px;font-size:21px;font-weight:500;color:#4a4a55;line-height:1.2}
.hero-title b{color:var(--yellow);font-weight:600}
.dots{display:flex;gap:6px}
.dots i{width:28px;height:6px;border:1.4px solid #9fd0ec;border-radius:4px;display:block}
.dots i.on{background:#9fd0ec}

/* sections */
.h2{font-size:20px;font-weight:500;color:var(--ink)}
.card{position:absolute;top:906px;width:169px;height:238px;background:#fff;box-shadow:0 2px 10px rgba(0,0,0,.1);border-radius:4px;overflow:hidden}
.card .pic{height:107px}
.card h3{font-size:10.4px;font-weight:500;color:var(--ink);margin:18px 0 0 22px;padding-bottom:6px;border-bottom:1px solid var(--line);width:135px}
.card p{font-size:8.6px;line-height:1.55;margin:8px 14px 0 22px}
.card a{display:inline-block;margin:8px 0 0 22px;font-size:9.5px;font-weight:600;color:var(--ink);text-decoration:none;border-bottom:2px solid var(--yellow);line-height:1.1}
.sub{font-size:14px;font-weight:600;color:var(--blue);letter-spacing:.4px}

/* feature text blocks: heading, copy and button flow so nothing overlaps */
.feature{position:absolute;width:360px}
.feature .para{position:static;margin-top:10px;font-size:8.9px;line-height:1.52;letter-spacing:-.05px}
.feature .para p{margin-bottom:10px}
.feature .para p:last-child{margin-bottom:12px}
.feature .btn{position:relative;width:85px;height:24px}

/* stats */
.stats{top:1902px;left:0;width:1200px;height:222px;background:linear-gradient(100deg,#6f86b4 0%,#c9c7e0 22%,#3b57a8 45%,#c79db8 62%,#3a58b0 78%,#7d95c9 100%)}
.stat{position:absolute;top:54px;width:120px;text-align:center;color:#fff}
.stat .ic{width:60px;height:60px;margin:0 auto;background:#fff;border-radius:3px;display:flex;align-items:center;justify-content:center}
.stat b{display:block;font-size:32px;font-weight:600;line-height:1;margin-top:10px}
.stat span{font-size:10px;font-weight:500}
.vline{position:absolute;top:40px;width:1px;height:140px;background:rgba(255,255,255,.25)}

/* testimonial */
.quote{top:2197px;left:341px;width:464px;height:219px;background:#fff;box-shadow:0 1px 10px rgba(0,0,0,.12);text-align:center}

/* form */
.form{top:2453px;left:643px;width:302px;height:311px;background:#fff;box-shadow:0 2px 12px rgba(0,0,0,.14)}
.field{position:absolute;left:13px;width:275px;height:23px;border:1px solid var(--line);display:flex;align-items:center;font-size:8.5px;color:#888}
.field i{width:24px;height:100%;border-right:1px solid var(--line);display:flex;align-items:center;justify-content:center;margin-right:7px}

/* footer */
.foot-text{color:#d8d8de;font-size:9.5px}
.foot h4{font-size:17px;font-weight:500;color:#fff}
.flinks a{position:absolute;color:#d8d8de;font-size:9.5px;text-decoration:none}
.soc{position:absolute;top:2973px;width:22px;height:22px;border:1.4px solid var(--blue);border-radius:50%}
</style>
</head>
<body>

<!-- Header -->
<div class="abs topline">
  <span><svg width="12" height="12" viewBox="0 0 24 24" fill="none" stroke="#555" stroke-width="1.8"><path d="M5 3l4 1 2 5-3 2a12 12 0 006 6l2-3 5 2 1 4-3 2C11 22 2 13 3 6z"/></svg>002-555-0187</span>
  <span><svg width="12" height="10" viewBox="0 0 24 18" fill="none" stroke="#555" stroke-width="1.8"><rect x="1" y="1" width="22" height="16"/><path d="M1 1l11 9 11-9"/></svg>info@brightlantern.com</span>
</div>
<div class="abs brand" style="top:13px;left:236px"><i></i>BRIGHT LANTERN</div>
<nav class="abs navbar">
  <a class="on" href="#">HOME</a><span class="sep">/</span>
  <a href="#">ABOUT US</a><span class="sep">/</span>
  <a href="#">SERVICES</a><span class="sep">/</span>
  <a href="#">TESTIMONIAL</a><span class="sep">/</span>
  <a href="#">BLOG</a><span class="sep">/</span>
  <a href="#">CONTACT US</a>
</nav>
<div class="abs" style="top:68px;left:0;width:1200px;height:1px;background:var(--line)"></div>

<!-- Hero -->
<svg class="abs" style="top:69px;left:0" width="700" height="425" viewBox="0 0 700 425" aria-hidden="true">
  <path d="M0 0H662C690 60 690 150 650 230C600 330 500 420 370 420C240 420 150 370 70 330C40 315 15 305 0 300Z" fill="var(--pink)"/>
</svg>
<div class="abs eyebrow"><span class="u">CREATIVE AGENCY</span></div>
<h1 class="abs hero-title"><b>DIGITAL MARKETING</b> for companies who know that <span class="u">BRIGHT LANTERN</span> counts.</h1>
<p class="para" style="top:315px;left:235px;width:380px;font-size:10px">We always help you to achieve the best in every digital transaction. Because like in real life, you don't get a second channel for your first impression.</p>
<div class="btn" style="top:384px;left:235px;width:85px;height:23px">Get Started</div>
<div class="art" role="img" aria-label="Isometric illustration of a large monitor with charts surrounded by people, money and analytics" style="top:75px;left:690px;width:452px;height:448px;background:radial-gradient(circle at 55% 40%,#f7a34a 0%,#f2c24c 22%,#e9ecf6 48%,#fff 72%)"></div>
<div class="abs dots" style="top:495px;left:554px"><i></i><i class="on"></i><i></i></div>

<!-- About -->
<div class="art" role="img" aria-label="Illustration of two people working on laptops in a pink living room" style="top:547px;left:235px;width:338px;height:279px;border-radius:48% 52% 45% 55%;background:linear-gradient(160deg,#fde4f0,#fbd4e6 60%,#fdeaf3)"></div>
<h2 class="abs h2" style="top:557px;left:600px"><span class="u">About Us</span></h2>
<div class="abs" style="top:599px;left:604px;font-size:18px;font-weight:500;color:var(--yellow);letter-spacing:.3px">WE ARE THE NUMBER #1 COMPANY</div>
<div class="para" style="top:626px;left:604px;width:355px;font-size:8.9px">
  <p>But I must explain to you how all this mistaken idea of denouncing pleasure and praising pain was born and I will give you a complete account of the system, and expound the actual teachings of the great explorer of the truth, the master-builder of human happiness.</p>
  <p>Sed ut perspiciatis unde omnis iste natus error sit voluptatem accusantium doloremque laudantium, totam rem aperiam, eaque ipsa quae ab illo inventore veritatis et quasi architecto beatae vitae dicta sunt explicabo.</p>
</div>

<!-- Services -->
<h2 class="abs h2" style="top:858px;left:0;width:1200px;text-align:center"><span class="u">Our Services</span></h2>
<div class="card" style="left:241px"><div class="pic" role="img" aria-label="Illustration of news and paid advertising" style="background:linear-gradient(135deg,#3a6fd8,#42b3ea)"></div><h3>Paid Advertising</h3><p>But I must explain to you how all this mistaken idea of denouncing pleasure and praising pain...</p><a href="#">View Details</a></div>
<div class="card" style="left:423px"><div class="pic" role="img" aria-label="Illustration of analytics dashboards and a magnifier" style="background:linear-gradient(135deg,#7ec3d8,#a9d8e4)"></div><h3>Analytics &amp; Optimization</h3><p>But I must explain to you how all this mistaken idea of denouncing pleasure and praising pain...</p><a href="#">View Details</a></div>
<div class="card" style="left:605px"><div class="pic" role="img" aria-label="Illustration of a laptop with chat bubbles and a bot" style="background:linear-gradient(135deg,#1f9be0,#2fb3ee)"></div><h3>Chatbots</h3><p>But I must explain to you how all this mistaken idea of denouncing pleasure and praising pain...</p><a href="#">View Details</a></div>
<div class="card" style="left:787px"><div class="pic" role="img" aria-label="Illustration of an online store with cart and delivery" style="background:linear-gradient(135deg,#a8dde0,#cdeef0)"></div><h3>E-commerce shops</h3><p>But I must explain to you how all this mistaken idea of denouncing pleasure and praising pain...</p><a href="#">View Details</a></div>

<!-- Win new customers -->
<svg class="abs" style="top:1177px;left:0" width="1200" height="405" viewBox="0 0 1200 405" aria-hidden="true"><polygon points="0,0 1200,22 1200,404 0,327" fill="var(--grey)"/></svg>
<div class="art" role="img" aria-label="Isometric illustration of two people working on laptops with chat bubbles" style="top:1213px;left:238px;width:321px;height:297px;background:radial-gradient(circle at 50% 55%,#d98ee3 0%,#a7b5ef 35%,#ececf3 70%,var(--grey) 100%)"></div>
<div class="feature" style="top:1248px;left:602px">
  <div class="sub">Win new Customets &amp; Employees!</div>
  <div class="para">
    <p>Sed ut perspiciatis unde omnis iste natus error sit voluptatem accusantium doloremque laudantium, totam rem aperiam, eaque ipsa quae ab illo inventore veritatis et quasi architecto beatae vitae dicta sunt explicabo. Nemo enim ipsam voluptatem quia voluptas sit aspernatur aut odit aut fugit, sed quia consequuntur magni dolores eos qui ratione voluptatem sequi nesciunt.</p>
    <p>Ut enim ad minima veniam, quis nostrum exercitationem ullam corporis suscipit laboriosam, nisi ut aliquid ex ea commodi consequatur? Quis autem vel eum iure reprehenderit qui in ea voluptate velit esse quam nihil molestiae consequatur, vel illum qui dolorem eum fugiat quo voluptas nulla pariatur?</p>
    <p>Nam libero tempore, cum soluta nobis est eligendi optio cumque nihil impedit quo minus id quod maxime placeat facere possimus, omnis voluptas assumenda est, omnis dolor repellendus.</p>
  </div>
  <div class="btn">Read More</div>
</div>

<!-- Online marketing -->
<div class="feature" style="top:1613px;left:235px">
  <div class="sub">Online-Marketing Business!</div>
  <div class="para">
    <p>Sed ut perspiciatis unde omnis iste natus error sit voluptatem accusantium doloremque laudantium, totam rem aperiam, eaque ipsa quae ab illo inventore veritatis et quasi architecto beatae vitae dicta sunt explicabo. Nemo enim ipsam voluptatem quia voluptas sit aspernatur aut odit aut fugit, sed quia consequuntur magni dolores eos qui ratione voluptatem sequi nesciunt.</p>
    <p>Ut enim ad minima veniam, quis nostrum exercitationem ullam corporis suscipit laboriosam, nisi ut aliquid ex ea commodi consequatur? Quis autem vel eum iure reprehenderit qui in ea voluptate velit esse quam nihil molestiae consequatur, vel illum qui dolorem eum fugiat quo voluptas nulla pariatur?</p>
    <p>Nam libero tempore, cum soluta nobis est eligendi optio cumque nihil impedit quo minus id quod maxime placeat facere possimus, omnis voluptas assumenda est, omnis dolor repellendus.</p>
  </div>
  <div class="btn">Read More</div>
</div>
<div class="art" role="img" aria-label="Illustration of a presenter showing a chart to a team at a meeting table" style="top:1635px;left:612px;width:339px;height:184px;background:linear-gradient(180deg,#f4f7fa,#e3ecf3 60%,#fff)"></div>

<!-- Stats -->
<section class="abs stats" role="img" aria-label="Blurred office photo background with key figures">
  <div class="stat" style="left:267px"><div class="ic"><svg width="28" height="28" viewBox="0 0 24 24" fill="none" stroke="#999" stroke-width="1.3"><circle cx="12" cy="8" r="4"/><path d="M4 21c0-5 4-7 8-7s8 2 8 7z"/></svg></div><b>780</b><span>Customers</span></div>
  <div class="vline" style="left:411px"></div>
  <div class="stat" style="left:449px"><div class="ic"><svg width="28" height="28" viewBox="0 0 24 24" fill="none" stroke="#999" stroke-width="1.3"><path d="M7 3h10v5a5 5 0 01-10 0z"/><path d="M7 5H3c0 3 2 5 4 5M17 5h4c0 3-2 5-4 5M12 13v4M8 21h8l-1-4H9z"/></svg></div><b>53</b><span>Awards</span></div>
  <div class="vline" style="left:596px"></div>
  <div class="stat" style="left:626px"><div class="ic"><svg width="30" height="28" viewBox="0 0 26 24" fill="none" stroke="#999" stroke-width="1.3"><circle cx="13" cy="7" r="3.5"/><circle cx="6" cy="9" r="2.5"/><circle cx="20" cy="9" r="2.5"/><path d="M7 20c0-4 3-7 6-7s6 3 6 7zM2 19c0-3 2-5 4-5M24 19c0-3-2-5-4-5"/></svg></div><b>100%</b><span>Marketing</span></div>
  <div class="vline" style="left:771px"></div>
  <div class="stat" style="left:802px"><div class="ic"><svg width="30" height="26" viewBox="0 0 26 22" fill="none" stroke="#999" stroke-width="1.3"><rect x="2" y="6" width="22" height="14" rx="1"/><path d="M9 6V3h8v3M2 12h22"/></svg></div><b>210K</b><span>Projects</span></div>
</section>

<!-- Testimonials -->
<h2 class="abs h2" style="top:2152px;left:0;width:1200px;text-align:center"><span class="u">Testimonials</span></h2>
<div class="abs quote">
  <div role="img" aria-label="Client portrait" style="width:60px;height:60px;margin:18px auto 0;background:linear-gradient(180deg,#8fd0f3,#3d8fd3)"></div>
  <div style="margin-top:12px;font-size:11px;font-weight:500;color:var(--ink);letter-spacing:.6px">DANIEL MARSH</div>
  <div style="font-size:7.5px;font-weight:500;color:#555;letter-spacing:.5px">FOUNDER</div>
  <p style="margin:12px 24px 0;font-size:9.5px;line-height:1.3">But I must explain to you how all this mistaken idea of denouncing pleasure and praising pain was born and I will give you a complete account of the system, and expound the actual teachings of the great explorer of the truth, the master-builder of human happiness.</p>
  <div class="dots" style="justify-content:center;margin-top:14px"><i></i><i class="on"></i><i></i></div>
</div>

<!-- Contact -->
<div class="art" role="img" aria-label="Street map showing the agency location" style="top:2481px;left:253px;width:390px;height:254px;border-radius:0;background:linear-gradient(135deg,#eceef1,#e3e6ea 60%,#dfe8df);box-shadow:0 1px 6px rgba(0,0,0,.15)"></div>
<div class="abs form">
  <h2 style="text-align:center;margin-top:12px;font-size:17px;font-weight:600;color:var(--ink)"><span class="u">Ask you Question</span></h2>
  <div class="field" style="top:50px"><i><svg width="9" height="9" viewBox="0 0 24 24" fill="#888"><circle cx="12" cy="7" r="5"/><path d="M2 23c0-6 5-9 10-9s10 3 10 9z"/></svg></i>Your Name</div>
  <div class="field" style="top:87px"><i><svg width="10" height="8" viewBox="0 0 24 18" fill="none" stroke="#888" stroke-width="2"><rect x="1" y="1" width="22" height="16"/><path d="M1 1l11 9 11-9"/></svg></i>Your Email</div>
  <div class="field" style="top:122px"><i><svg width="9" height="9" viewBox="0 0 24 24" fill="#888"><path d="M5 2l4 1 2 5-3 2a12 12 0 006 6l2-3 5 2 1 4-3 3C11 22 2 13 2 5z"/></svg></i>Telephone Number</div>
  <div class="field" style="top:158px"><i><svg width="10" height="9" viewBox="0 0 26 22" fill="#888"><rect x="2" y="6" width="22" height="14"/><path d="M9 6V3h8v3" stroke="#888" stroke-width="2" fill="none"/></svg></i>Your Business</div>
  <div class="btn" style="top:202px;left:114px;width:73px;height:22px">SUBMIT</div>
  <div style="position:absolute;top:244px;left:84px;display:flex;align-items:center;gap:8px;font-size:11px;color:var(--ink)">
    <div role="img" aria-label="Contact person portrait" style="width:28px;height:28px;border-radius:50%;background:linear-gradient(180deg,#c9a58f,#6b5b55)"></div>
    <svg width="13" height="13" viewBox="0 0 24 24" fill="none" stroke="#666" stroke-width="1.6"><path d="M5 3l4 1 2 5-3 2a12 12 0 006 6l2-3 5 2 1 4-3 2C11 22 2 13 3 6z"/></svg>002-555-0187
  </div>
</div>

<!-- Footer -->
<svg class="abs" style="top:2776px;left:0" width="1200" height="286" viewBox="0 0 1200 286" aria-hidden="true">
  <path d="M0 70C200 20 400 8 600 18C850 30 1050 20 1200 0V286H0Z" fill="var(--yellow)"/>
  <path d="M0 76C200 28 400 16 600 26C850 38 1050 28 1200 8V286H0Z" fill="var(--footer)"/>
</svg>
<footer class="foot">
  <div class="abs brand" style="top:2867px;left:236px;color:#fff"><i style="background:#fff"></i>BRIGHT LANTERN</div>
  <p class="abs foot-text" style="top:2915px;left:236px;width:250px;line-height:1.35">But I must explain to you how all this mistaken idea of denouncing pleasure and praising pain was born and I will give you a complete account of the system.</p>
  <i class="soc" style="left:236px"></i><i class="soc" style="left:266px"></i><i class="soc" style="left:296px"></i>
  <h4 class="abs" style="top:2864px;left:546px"><span class="u">Important Links</span></h4>
  <div class="flinks">
    <a style="top:2917px;left:546px">Home</a><a style="top:2937px;left:546px">About Us</a><a style="top:2957px;left:546px">Contact Us</a><a style="top:2977px;left:546px">Get a quote</a>
    <a style="top:2917px;left:659px">Blog</a><a style="top:2937px;left:659px">Services</a><a style="top:2957px;left:659px">Project</a><a style="top:2977px;left:659px">Privacy policy</a>
  </div>
  <h4 class="abs" style="top:2864px;left:787px"><span class="u">Get in Touch</span></h4>
  <div class="abs foot-text" style="top:2919px;left:788px;display:flex;gap:8px;line-height:1.3"><svg width="12" height="16" viewBox="0 0 12 16" fill="none" stroke="var(--blue)" stroke-width="1.3"><path d="M6 15S1 9 1 6a5 5 0 0110 0c0 3-5 9-5 9z"/><circle cx="6" cy="6" r="2"/></svg><span>48 Harbor Lane<br>Fairview, USA</span></div>
  <div class="abs foot-text" style="top:2962px;left:788px;display:flex;gap:8px"><svg width="13" height="13" viewBox="0 0 24 24" fill="none" stroke="var(--blue)" stroke-width="1.6"><path d="M5 3l4 1 2 5-3 2a12 12 0 006 6l2-3 5 2 1 4-3 2C11 22 2 13 3 6z"/></svg>002-555-0187</div>
  <div class="abs foot-text" style="top:2993px;left:788px;display:flex;gap:8px"><svg width="14" height="11" viewBox="0 0 24 18" fill="none" stroke="var(--blue)" stroke-width="1.6"><rect x="1" y="1" width="22" height="16"/><path d="M1 1l11 9 11-9"/></svg>info@brightlantern.com</div>
  <div class="abs" style="top:3030px;left:0;width:1200px;height:1px;background:#333338"></div>
  <div class="abs" style="top:3041px;left:0;width:1200px;text-align:center;font-size:8px;color:#ccc">Copyright © 2020, <span style="color:var(--blue)">BRIGHT LANTERN.</span></div>
</footer>

</body>
</html>
```